MRHT Needs Fundraiser Dinner Invite!!

The Marisol Hendrick Trust, a 501 3(c) non for profit has a yearly fundraiser, with varying themes. Last year it was "cowboys" and "cowgirls"
This year, it is Club Orchid, or 70's disco music. I have uploaded last years invite for reference, some stock photography for inspiration. You are not limited to using the stock photos.

Annual MRHT Fundraiser Dinner
October 13th, 2022
Starts: 6:30pm
RSVP By: September 20th
Place: The Bramwell
Price: $135 per ticket

Target Market(s)

Donors, Business People, Every person

Industry/Entity Type

Non for Profit

Font styles to use
Sans Serif

Colors
0054AA
0677BA
7BADD7
CADEEF
E8F1F8
E54698
E96AAD
F1A4CE
F9D9EA
FCEFF6
6B429C
8869AF
B7A5CE
E3DAEB
F3F0F8

Requirements
Must have
• The invite should be 5x7, be sophisticated as the clientele are mainly business people that come to support the cause. It should be fun and inviting at the same time.

```html
<!DOCTYPE html>
<html lang="en">
<head>
<meta charset="utf-8">
<title>Annual MRHT Fundraising Dinner Invitation</title>
<link rel="stylesheet" href="https://fonts.googleapis.com/css2?family=Fredoka:wght@600;700&family=Oswald:wght@400;600&family=Poppins:wght@400;500&display=swap">
<style>
  :root {
    --purple-deep: #2e1748;
    --purple-dark: #4a2672;
    --purple: #6B429C;
    --purple-mid: #8869AF;
    --purple-light: #B7A5CE;
    --purple-pale: #E3DAEB;
    --pink: #E96AAD;
    --pink-soft: #F1A4CE;
    --white: #ffffff;
    --black: #111111;
  }
  * { margin: 0; padding: 0; box-sizing: border-box; }
  html, body { width: 783px; height: 1200px; overflow: hidden; background: var(--purple-deep); }
  .invite {
    position: relative;
    width: 783px;
    height: 1200px;
    overflow: hidden;
    background: var(--purple);
    font-family: "Poppins", sans-serif;
    color: var(--white);
  }
  .backdrop { position: absolute; inset: 0; }
  .invite-tag {
    position: absolute;
    left: 18px;
    top: -4px;
    width: 44px;
    height: 226px;
    background: var(--black);
    border: 3px solid var(--white);
    border-top: none;
    display: flex;
    align-items: center;
    justify-content: center;
  }
  .invite-tag span {
    transform: rotate(-90deg);
    white-space: nowrap;
    font-family: "Oswald", sans-serif;
    font-size: 34px;
    letter-spacing: 1px;
    color: var(--white);
  }
  .disco-frame {
    position: absolute;
    left: 206px;
    top: 37px;
    width: 370px;
    height: 370px;
    border-radius: 50%;
    background: var(--black);
    border: 4px solid var(--white);
    box-shadow: 0 0 0 6px var(--black);
    display: flex;
    align-items: center;
    justify-content: center;
  }
  .disco-ball {
    width: 322px;
    height: 322px;
    border-radius: 50%;
    background: radial-gradient(circle at 38% 32%, var(--pink-soft) 0%, var(--pink) 30%, var(--purple-mid) 60%, var(--purple-dark) 100%);
  }
  .title {
    position: absolute;
    top: 592px;
    left: 0;
    width: 100%;
    text-align: center;
    font-family: "Fredoka", sans-serif;
    font-weight: 700;
    line-height: 1;
    text-transform: uppercase;
  }
  .title .line { display: block; font-size: 76px; letter-spacing: 1px; }
  .title .line + .line { margin-top: 2px; }
  .title .line-big { font-size: 122px; margin-top: 4px; }
  .details {
    position: absolute;
    top: 878px;
    width: 100%;
    text-align: center;
    font-size: 31px;
    line-height: 1.3;
  }
  .date-box {
    position: absolute;
    left: 287px;
    top: 978px;
    width: 212px;
    background: var(--white);
    border: 4px solid var(--black);
    color: var(--black);
    font-family: "Oswald", sans-serif;
    text-align: center;
    font-size: 50px;
    line-height: 1.02;
    padding: 2px 0 4px;
    text-transform: uppercase;
  }
  .time-box {
    position: absolute;
    left: 287px;
    top: 1094px;
    width: 212px;
    background: var(--white);
    border: 4px solid var(--black);
    color: var(--black);
    font-family: "Oswald", sans-serif;
    font-weight: 600;
    text-align: center;
    font-size: 38px;
    line-height: 1.2;
  }
  .butterflies {
    position: absolute;
    left: 595px;
    top: 940px;
    width: 140px;
    height: 130px;
    border-radius: 40% 50% 45% 50%;
    background: linear-gradient(135deg, var(--purple-light), var(--purple-mid));
    opacity: 0.55;
  }
  .rsvp {
    position: absolute;
    top: 1157px;
    width: 100%;
    text-align: center;
    font-size: 26px;
  }
</style>
</head>
<body>
<main class="invite">
  <svg class="backdrop" width="783" height="1200" viewBox="0 0 783 1200" aria-hidden="true">
    <defs>
      <linearGradient id="bg-main" x1="0" y1="0" x2="0" y2="1">
        <stop offset="0" stop-color="#5a3388"/>
        <stop offset="1" stop-color="#6B429C"/>
      </linearGradient>
      <linearGradient id="band-dark" x1="0" y1="0" x2="1" y2="1">
        <stop offset="0" stop-color="#2e1748"/>
        <stop offset="1" stop-color="#4a2672"/>
      </linearGradient>
    </defs>
    <rect width="783" height="1200" fill="url(#bg-main)"/>
    <polygon points="0,0 783,0 783,620 0,260" fill="url(#band-dark)"/>
    <g stroke="#8869AF" stroke-width="3" opacity="0.55">
      <line x1="0" y1="150" x2="783" y2="510"/>
      <line x1="0" y1="180" x2="783" y2="540"/>
      <line x1="0" y1="210" x2="783" y2="570"/>
      <line x1="0" y1="240" x2="783" y2="600"/>
    </g>
    <polygon points="0,760 500,1200 0,1200" fill="#8869AF" opacity="0.55"/>
    <polygon points="0,960 300,1200 0,1200" fill="#B7A5CE" opacity="0.5"/>
    <polygon points="783,820 783,1200 560,1200" fill="#4a2672" opacity="0.5"/>
  </svg>

  <div class="invite-tag"><span>INVITATION</span></div>

  <div class="disco-frame">
    <div class="disco-ball" role="img" aria-label="Sparkling purple and pink mirrored disco ball"></div>
  </div>

  <h1 class="title">
    <span class="line">Annual MRHT</span>
    <span class="line">Fundraising</span>
    <span class="line line-big">Dinner</span>
  </h1>

  <p class="details">Place: The Bramwell<br>Price: $135 per ticket</p>

  <div class="date-box">October<br>13th 2022</div>
  <div class="time-box">6:30 PM</div>

  <div class="butterflies" role="img" aria-label="Pair of line-drawn butterflies"></div>

  <p class="rsvp">RSVP By: September 20th</p>
</main>
</body>
</html>
```